Financial Coaching & Personal Development

I’m desiring a classic business card for my financial coaching and personal development business. The colors I have started with are a goldish brown and hunter green. The brownish color represents soil and green represents growth. I don’t want it it to look masculine. I want the brown to be more of a golden color. I want the color combination and overall design to be timeless not trendy. The logo can be changed as long as it represents growth- moving from where you are to where you want to be.

Target Market(s)

Working Adults with median income $65k; small businesses with a minimum of 20 employees

Industry/Entity Type

Consulting

Contact Information for Business Card

Marla Quenby, MBA
Certified Financial Coach

Font styles to use
Serif

Requirements
Must have
• Logo
My name
Business description
Email marla.quenby@thrivelanefundhouse
Phone number 662-555-0187
Nice to have
• Slogan

```html
<!DOCTYPE html>
<html lang="en">
<head>
<meta charset="utf-8">
<title>Thrivelane Fund House – Business Card</title>
<link rel="stylesheet" href="https://fonts.googleapis.com/css2?family=Arimo:wght@400;700&family=Tinos:wght@400;700&display=swap">
<style>
  :root {
    --page-bg: #2a2a2a;
    --card-bg: #0d0d0d;
    --gold: #8a6a12;
    --green: #2aa310;
    --white: #f2f2f2;
    --silver: #c9c9c9;
  }
  * { margin: 0; padding: 0; box-sizing: border-box; }
  html, body { width: 1200px; height: 900px; overflow: hidden; }
  body {
    background: var(--page-bg);
    font-family: "Arimo", Arial, sans-serif;
    display: flex;
    flex-direction: column;
    align-items: center;
    justify-content: center;
    gap: 40px;
  }
  .card {
    width: 700px;
    height: 400px;
    background: var(--card-bg);
    border-radius: 26px;
    position: relative;
    overflow: hidden;
  }
  .brand {
    position: absolute;
    left: 0; right: 0;
    text-align: center;
  }
  .brand-name {
    display: inline-flex;
    align-items: center;
    gap: 12px;
    font-weight: 700;
    font-size: 30px;
    letter-spacing: 2px;
    text-transform: uppercase;
  }
  .brand-dot {
    width: 18px; height: 18px; border-radius: 50%;
  }
  .brand-tagline {
    font-family: "Tinos", "Times New Roman", serif;
    font-size: 15px;
    margin-top: 4px;
  }
  /* front */
  .card-front .brand { top: 70px; left: 200px; right: 30px; }
  .card-front .brand-name { color: var(--gold); }
  .card-front .brand-dot { background: var(--gold); }
  .card-front .brand-tagline { color: var(--green); }
  .contact {
    position: absolute;
    left: 50px;
    top: 180px;
    color: var(--white);
  }
  .person-name {
    color: var(--gold);
    font-size: 26px;
    font-weight: 700;
    text-transform: uppercase;
  }
  .person-title { font-size: 22px; margin-bottom: 12px; }
  .contact-list { list-style: none; font-size: 19px; line-height: 1.45; }
  .contact-list li { display: flex; align-items: center; gap: 10px; }
  .contact-list svg { width: 20px; height: 20px; flex: none; }
  .slogan {
    position: absolute;
    left: 50px;
    bottom: 34px;
    font-family: "Tinos", "Times New Roman", serif;
    font-weight: 700;
    font-size: 30px;
    color: var(--green);
  }
  /* back */
  .card-back .brand { top: 120px; }
  .card-back .brand-name { color: var(--silver); }
  .card-back .brand-dot { background: var(--silver); }
  .card-back .brand-tagline { color: var(--silver); }
  .services {
    position: absolute;
    left: 0; right: 0; top: 250px;
    text-align: center;
    color: var(--white);
    font-size: 19px;
    line-height: 1.4;
  }
</style>
</head>
<body>
  <section class="card card-front">
    <div class="brand">
      <div class="brand-name"><span class="brand-dot"></span>Thrivelane Fund House</div>
      <div class="brand-tagline">Financial Education &amp; Personal Development</div>
    </div>
    <div class="contact">
      <div class="person-name">Marla Quenby, MBA</div>
      <div class="person-title">Certified Financial Coach</div>
      <ul class="contact-list">
        <li>
          <svg viewBox="0 0 24 24" aria-hidden="true"><path fill="#8a6a12" d="M6.6 10.8a15 15 0 0 0 6.6 6.6l2.2-2.2c.3-.3.7-.4 1-.2 1.1.4 2.3.6 3.6.6.6 0 1 .4 1 1V20c0 .6-.4 1-1 1A17 17 0 0 1 3 4c0-.6.4-1 1-1h3.5c.6 0 1 .4 1 1 0 1.3.2 2.5.6 3.6.1.3 0 .7-.2 1z"/></svg>
          662-555-0187
        </li>
        <li>
          <svg viewBox="0 0 24 24" aria-hidden="true"><rect x="2" y="5" width="20" height="14" fill="#8a6a12"/><path d="M2 5l10 8 10-8" fill="none" stroke="#0d0d0d" stroke-width="1.6"/></svg>
          marla.quenby@thrivelanefundhouse.com
        </li>
        <li>
          <svg viewBox="0 0 24 24" aria-hidden="true"><g fill="none" stroke="#8a6a12" stroke-width="1.8"><circle cx="12" cy="12" r="9"/><ellipse cx="12" cy="12" rx="4" ry="9"/><path d="M3 12h18M5 7h14M5 17h14"/></g></svg>
          www.thrivelanefundhouse.com
        </li>
      </ul>
    </div>
    <div class="slogan">Create a Financial Plan that makes you Smile!</div>
  </section>

  <section class="card card-back">
    <div class="brand">
      <div class="brand-name"><span class="brand-dot"></span>Thrivelane Fund House</div>
      <div class="brand-tagline">Financial Education &amp; Personal Development</div>
    </div>
    <div class="services">
      Personal Financial Coaching &nbsp;|&nbsp; Financial Workshops for Youth<br>
      Employee Financial Wellness and Development
    </div>
  </section>
</body>
</html>
```